Brierley Dunmore Lawyers needs a web design

We need a web design for our conveyancing and commercial law firm based in Sydney Australia. We want to depersonalise the current website: http://www.brierleydunmore.example/ and give it a classic modern feel to it. It should be a simple design (possibly one page) and communicate trust, professionalism and experience.

Content should include:

Brierley Dunmore is a boutique Sydney based legal practice specialising in business and property law.

We pride ourselves on our proactive, receptive and dynamic approach to client service. Our business survives on referrals from satisfied clients and professionals who respect the way we do business.

Practice areas

Business law

We act on the sale and purchase of businesses. We assist clients with structuring their businesses, drafting shareholder agreements and buy-sell arrangements. We have acted on a multitude of other commercial matters including franchising, distribution, marketing and business services (with a particular focus in the advertising sector).

Property law

We act for developers, commercial property investors, landlords and tenants. We also handle residential conveyancing and deal with strata and company title matters.

Private Client

We draft wills and codicils on behalf of clients and can also assist with applications for probate should the need arise.

Contact Us

Brierley Dunmore
Level 29, Wexcombe Tower
7 Marlowe Square
Sydney, NSW 2000

t: +61 (0)2 9471 6203
f: +61 (0)2 8526 4079
e: enquiries@brierleydunmore.example

Target Market(s)

Individuals and business who need legal advice in the area of property and commercial law

Industry/Entity Type

Legal

Number of Pages Required

1 page

Font styles to use
Sans Serif

Requirements
Must have
• Clear and concise content.
Nice to have
• Some images to break up the content.
Should not have
• Any offensive images tones or connotations.

```html
<!DOCTYPE html>
<html lang="en">
<head>
<meta charset="utf-8">
<title>Brierley Dunmore Lawyers</title>
<link href="https://fonts.googleapis.com/css2?family=Raleway:wght@300;400;500&family=Open+Sans:wght@400;600&family=Roboto:wght@500&display=swap" rel="stylesheet">
<style>
:root{
  --blue:#1447a0;
  --blue-dark:#123f8e;
  --ink:#0b0b0c;
  --white:#ffffff;
  --grey-btn:#7d7d7d;
  --muted:#b9c3d6;
}
*{margin:0;padding:0;box-sizing:border-box}
html,body{width:1081px;height:1200px;overflow:hidden;background:var(--ink)}
body{position:relative;font-family:'Open Sans',sans-serif;color:var(--white)}
.abs{position:absolute}

.hero-photo{left:0;top:0;width:1081px;height:894px;
  background:
    radial-gradient(ellipse 420px 300px at 820px 560px,rgba(210,200,180,.55),transparent 70%),
    radial-gradient(ellipse 300px 260px at 180px 320px,rgba(150,90,50,.55),transparent 70%),
    linear-gradient(120deg,#3a2a22 0%,#2b2b30 40%,#1e2028 70%,#3a3a40 100%);}
.header-bar{left:0;top:0;width:1081px;height:128px;background:rgba(0,0,0,.62)}
.services-band{left:0;top:626px;width:1081px;height:268px;background:rgba(5,5,6,.82)}

.brand{left:60px;top:38px;font-family:'Raleway',sans-serif;font-weight:500;color:var(--white);text-align:right}
.brand-name{font-size:24px;line-height:28px;display:block}
.brand-sub{font-size:13px;line-height:16px;display:block}

.nav a{position:absolute;top:0;height:91px;line-height:122px;font-family:'Open Sans',sans-serif;font-size:12px;font-weight:600;color:var(--white);text-decoration:none;white-space:nowrap}
.nav .active{left:448px;width:78px;background:var(--blue);text-align:center}

.headline{left:0;top:300px;width:1081px;text-align:center;font-family:'Raleway',sans-serif;font-weight:300;font-size:58px;line-height:62px;letter-spacing:-.5px}

.slider-dots{left:483px;top:493px;width:114px;height:43px;background:rgba(60,60,62,.85);border-radius:3px}
.dot{position:absolute;top:15px;width:12px;height:12px;border-radius:50%;background:var(--white)}
.dot.on{background:var(--blue)}

.service{top:660px;width:240px;text-align:center}
.service svg{display:block;margin:0 auto}
.service h3{font-family:'Raleway',sans-serif;font-weight:500;font-size:16px;margin-top:32px}
.service p{font-size:10.5px;line-height:12.5px;margin:10px auto 0;width:180px}
.btn-more{display:inline-block;margin-top:16px;width:64px;height:29px;line-height:29px;font-size:11px;border-radius:2px;background:linear-gradient(#f2f2f2,#c9c9c9);color:#2a4f8f}
.btn-more.primary{background:var(--blue);color:var(--white)}

.footer{left:0;top:894px;width:1081px;height:240px;background:var(--blue)}
.divider{top:14px;width:1px;height:212px;background:var(--blue-dark);box-shadow:1px 0 0 rgba(255,255,255,.06)}
.footer h4{position:absolute;font-family:'Roboto',sans-serif;font-weight:500;font-size:15px;letter-spacing:.2px}
.footer p{position:absolute;font-size:10.6px;line-height:15.3px}
.about-text{left:45px;top:68px;width:330px;text-align:justify}
.btn-grey{position:absolute;background:var(--grey-btn);color:var(--white);text-align:center;font-size:11px}
.read-more{left:46px;top:186px;width:94px;height:33px;line-height:33px}
.email-field{left:471px;top:127px;width:266px;height:33px;background:var(--white);color:#aaa;font-size:10px;line-height:33px;padding-left:11px}
.subscribe{left:471px;top:170px;width:266px;height:33px;line-height:33px;font-size:13px;letter-spacing:.3px}
.loc-row{position:absolute;left:850px;font-size:11px;line-height:15.5px;letter-spacing:.2px}
.loc-row svg{position:absolute;left:0;top:3px}
.loc-row span{display:block;padding-left:19px}

.copyright{left:0;top:1161px;width:1071px;text-align:center;font-family:'Raleway',sans-serif;font-size:10px}
.social{top:1154px;width:26px;height:25px;border:1px solid var(--blue)}
.social.filled{background:var(--blue)}
</style>
</head>
<body>

<div class="abs hero-photo" role="img" aria-label="Blurred photo of a lawyer in a suit reading a book in front of law library shelves"></div>
<div class="abs header-bar"></div>
<div class="abs services-band"></div>

<div class="abs brand"><span class="brand-name">Brierley Dunmore</span><span class="brand-sub">Lawyers</span></div>

<nav class="nav">
  <a class="active" href="#">HOME</a>
  <a style="left:557px" href="#">OUR PEOPLE</a>
  <a style="left:679px" href="#">PRACTICE AREAS</a>
  <a style="left:826px" href="#">TESTIMONIALS</a>
  <a style="left:960px" href="#">CONTACT US</a>
</nav>

<h1 class="abs headline">REALIZE YOUR CONSTITUTIONAL<br>RIGHT WITH QUALIFIED HELP</h1>

<div class="abs slider-dots">
  <span class="dot" style="left:32px"></span>
  <span class="dot on" style="left:55px"></span>
  <span class="dot" style="left:78px"></span>
</div>

<section class="abs service" style="left:93px">
  <svg width="64" height="52" viewBox="0 0 64 52" aria-hidden="true">
    <g fill="#1a4fb0" stroke="#0d2f70" stroke-width="1.5">
      <path d="M22 2l12 6v12l-12 6-12-6V8z"/>
      <path d="M12 22l12 6v12l-12 6L0 40V28z"/>
      <path d="M40 22l12 6v12l-12 6-12-6V28z"/>
      <path d="M34 12l12 6v8l-12-6z"/>
    </g>
  </svg>
  <h3>Business law</h3>
  <p>We act on the sale and purchase of businesses. We assist clients with structuring</p>
  <a class="btn-more primary">MORE</a>
</section>

<section class="abs service" style="left:420px">
  <svg width="48" height="42" viewBox="0 0 48 42" aria-hidden="true">
    <path fill="#fff" d="M24 2L2 22h6v18h12V28h8v12h12V22h6z"/>
    <path fill="none" stroke="#fff" stroke-width="2" d="M2 20L24 1l22 19"/>
  </svg>
  <h3 style="margin-top:29px">Property law</h3>
  <p>We act for developers, commercial property investors, landlords and tenants.</p>
  <a class="btn-more">MORE</a>
</section>

<section class="abs service" style="left:727px">
  <svg width="42" height="46" viewBox="0 0 42 46" aria-hidden="true">
    <circle cx="21" cy="12" r="11" fill="#fff"/>
    <path fill="#fff" d="M2 44c0-12 8-19 19-19s19 7 19 19z"/>
  </svg>
  <h3 style="margin-top:38px">Private Client</h3>
  <p>We draft wills and codicils on behalf of clients and can also assist with applications</p>
  <a class="btn-more">MORE</a>
</section>

<footer class="abs footer">
  <div class="abs divider" style="left:420px"></div>
  <div class="abs divider" style="left:797px"></div>

  <h4 style="left:47px;top:32px">ABOUT US</h4>
  <p class="about-text">Lorem ipsum dolor sit amet, consectetur adipiscing elit, sed do eiusmod tempor incididunt ut labore et dolore magna aliqua. Ut enim ad minim veniam, quis nostrud exercitation ullamco laboris nisi ut aliquip ex ea commodo consequat. Duis aute irure dolor in reprehenderit in voluptate velit esse cillum dolore eu fugiat nulla pariatur.</p>
  <div class="btn-grey read-more">READ MORE</div>

  <h4 style="left:469px;top:33px">NEWSLETTER SIGNUP</h4>
  <p style="left:469px;top:68px;width:280px">Subscribe our newsletter to know our daily updates and offer daily updates and offerpsun dolor sit amet elit, sed aliqua.</p>
  <div class="abs email-field">Enter your Email Id</div>
  <div class="btn-grey subscribe">SUBSCRIBE</div>

  <h4 style="left:850px;top:32px">LOCATION</h4>
  <div class="loc-row" style="top:70px">
    <svg width="9" height="12" viewBox="0 0 9 12"><path fill="#fff" d="M4.5 0A4.5 4.5 0 0 0 0 4.5C0 8 4.5 12 4.5 12S9 8 9 4.5A4.5 4.5 0 0 0 4.5 0zm0 6.3a1.8 1.8 0 1 1 0-3.6 1.8 1.8 0 0 1 0 3.6z"/></svg>
    <span>Brierley Dunmore<br>Level 29, Wexcombe Tower<br>7 Marlowe Square<br>Sydney, NSW 200</span>
  </div>
  <div class="loc-row" style="top:136px">
    <svg width="11" height="11" viewBox="0 0 11 11"><path fill="#fff" d="M2.2 0l2 2.6-1.1 1.4c.7 1.6 2.3 3.2 3.9 3.9l1.4-1.1L11 8.8 9.7 11C4.5 10.6.4 6.5 0 1.3z"/></svg>
    <span>Office:&nbsp; +61 (0)2 9471 6203</span>
  </div>
  <div class="loc-row" style="top:157px">
    <svg width="11" height="11" viewBox="0 0 11 11"><rect x="2" y="0" width="7" height="4" fill="#fff"/><rect x="0" y="4" width="11" height="7" rx="1" fill="#fff"/><rect x="2" y="6" width="7" height="1.5" fill="#1447a0"/></svg>
    <span>Fax:&nbsp; +61 (0)2 8526 4079</span>
  </div>
  <div class="loc-row" style="top:177px">
    <svg width="11" height="9" viewBox="0 0 11 9"><rect width="11" height="9" fill="#fff"/><path d="M0 0l5.5 5L11 0" fill="none" stroke="#1447a0" stroke-width="1.2"/></svg>
    <span>enquiries@brierleydunmore.example</span>
  </div>
</footer>

<p class="abs copyright">Copyright 2015 Comapny name. All Rights Reserved.</p>
<div class="abs social" style="left:945px"></div>
<div class="abs social filled" style="left:978px"></div>
<div class="abs social" style="left:1012px"></div>

</body>
</html>
```